I need a newspaper ads that suits events / outings all over the world. refreshing feeling that suits my company logo.
Size of the ads is 6cm by 6cm a square
takenote
1) Joining up as members is free .
2) Places of interest tickets discount for members
3) Special events / outings host almost everyday
4) main point is everyone able to know each another
website : www.WanderNookly.com
Target Market(s)
Targeting general age 18-40 . mainly singles
contents to put inside the ads
2) Local Places of interest tickets discount for members
4) Website : www.WanderNookly.com
5) We also host photos contest
6) Meet the different faces of the world
7) Experience Sharing Gathering !
Industry/Entity Type
It Company
Requirements
Must have
- Refreshing feeling , and professional . will be uploading more pictures , kindly put some pictures combine into it to make people feel there is a lot activities can be involve when they join as member.

```html
<!DOCTYPE html>
<html lang="en">
<head>
<meta charset="utf-8">
<title>Gate to the New World – Nookly Events</title>
<link rel="stylesheet" href="https://fonts.googleapis.com/css2?family=Open+Sans:wght@400;600;700&family=Roboto+Condensed:ital,wght@0,400;1,400;1,500&display=swap">
<style>
  :root {
    --sky-top: #7a7a7a;
    --sky-low: #b4b4b4;
    --sea: #9c9c9c;
    --sand: #e8e8e8;
    --ink: #2f2f2f;
    --ink-soft: #4a4a4a;
    --white: #ffffff;
    --band: #555555;
    --ribbon: #5a5a5a;
    --badge: #5c5c5c;
    --frame: #f7f7f7;
    --photo: #8f8f8f;
    --swoosh: #d0d0d0;
  }
  * { margin: 0; padding: 0; box-sizing: border-box; }
  html, body { width: 1200px; height: 1200px; overflow: hidden; background: #ffffff; }
  .ad {
    position: relative; width: 1200px; height: 1200px; overflow: hidden;
    font-family: "Roboto Condensed", "Arial Narrow", sans-serif; color: var(--ink);
  }
  .scenery {
    position: absolute; inset: 0;
    background: linear-gradient(180deg, var(--sky-top) 0%, var(--sky-low) 22%, #8a8a8a 32%, #a6a6a6 45%, var(--sea) 55%, #cfcfcf 68%, var(--sand) 82%, #f2f2f2 100%);
  }
  .headline { position: absolute; inset: 0; color: var(--white); font-family: "Open Sans", Arial, sans-serif; white-space: nowrap; }
  .headline .lead { position: absolute; left: 183px; top: 50px; font-size: 44px; font-weight: 600; line-height: 54px; letter-spacing: -1px; }
  .headline .main { position: absolute; left: 378px; top: 44px; font-size: 112px; font-weight: 700; letter-spacing: -4px; line-height: 1; }
  .headline .tagline { position: absolute; left: 745px; top: 150px; font-size: 28px; font-weight: 400; line-height: 1.2; }

  .string { position: absolute; left: 0; top: 300px; width: 1200px; height: 40px; }
  .snapshot {
    position: absolute; background: var(--frame); padding: 12px 12px 32px;
    box-shadow: 0 4px 10px rgba(0,0,0,.35);
  }
  .snapshot .shot { width: 100%; height: 100%; background: linear-gradient(160deg, #a5a5a5, var(--photo) 55%, #6e6e6e); }
  .snapshot .clip { position: absolute; top: -22px; left: 50%; width: 14px; height: 38px; margin-left: -7px; border: 3px solid #9a9a9a; border-radius: 7px; }
  .snap-1 { left: 8px; top: 318px; width: 258px; height: 238px; transform: rotate(-4deg); }
  .snap-2 { left: 291px; top: 308px; width: 250px; height: 265px; transform: rotate(2deg); }
  .snap-3 { left: 618px; top: 313px; width: 254px; height: 262px; transform: rotate(1deg); }
  .snap-4 { left: 905px; top: 325px; width: 270px; height: 265px; transform: rotate(10deg); }

  .ribbon { position: absolute; left: 34px; top: 592px; width: 568px; height: 60px; }
  .ribbon-text { position: absolute; left: 80px; top: 600px; color: var(--white); font-style: italic; font-size: 32px; line-height: 44px; white-space: nowrap; }

  .perks { position: absolute; inset: 0; }
  .perk { position: absolute; white-space: nowrap; font-style: italic; font-size: 27px; color: var(--ink-soft); letter-spacing: -.3px; }
  .perk em { font-style: italic; font-weight: 500; font-size: 47px; color: var(--ink); letter-spacing: -1px; }
  .perk-1 { left: 93px; top: 670px; }
  .perk-1 em { font-size: 44px; }
  .perk-2 { left: 254px; top: 738px; }
  .perk-3 { left: 127px; top: 806px; }
  .perk-3 em { font-size: 41px; }
  .perk-4 { left: 322px; top: 862px; }
  .perk-5 { left: 313px; top: 928px; }
  .perk-6 { left: 406px; top: 985px; }

  .swoosh { position: absolute; left: 0; top: 960px; width: 1200px; height: 170px; }
  .badge { position: absolute; left: 889px; top: 720px; width: 236px; height: 236px; }

  .brand { position: absolute; left: 130px; top: 920px; width: 190px; text-align: center; }
  .brand .mark { width: 72px; height: 72px; margin: 0 auto 10px; border-radius: 50%; background: var(--ink-soft); }
  .brand .name { font-family: "Roboto Condensed", "Arial Narrow", sans-serif; font-size: 30px; color: var(--ink-soft); letter-spacing: 1px; white-space: nowrap; }

  .contact-bar {
    position: absolute; left: 0; top: 1121px; width: 1200px; height: 79px; background: var(--band);
    color: var(--white); font-family: "Open Sans", Arial, sans-serif; font-size: 31px;
  }
  .contact { position: absolute; top: 0; height: 79px; display: flex; align-items: center; gap: 22px; white-space: nowrap; }
  .contact-mail { left: 40px; }
  .contact-web { left: 705px; }
</style>
</head>
<body>
<main class="ad">
  <div class="scenery" role="img" aria-label="Tropical bay with a limestone island, calm sea, a long-tail boat and a sandy beach"></div>

  <header class="headline">
    <div class="lead">GATE<br>TO THE</div>
    <h1 class="main">NEW WORLD</h1>
    <p class="tagline">Meet with Happiness!</p>
  </header>

  <svg class="string" viewBox="0 0 1200 40" aria-hidden="true">
    <path d="M0 12 Q600 22 1200 8" fill="none" stroke="#5e5e5e" stroke-width="3"/>
  </svg>

  <figure class="snapshot snap-1"><span class="clip"></span><div class="shot" role="img" aria-label="Member posing beside a temple statue"></div></figure>
  <figure class="snapshot snap-2"><span class="clip"></span><div class="shot" role="img" aria-label="Traditional dancers in ornate costumes on stage"></div></figure>
  <figure class="snapshot snap-3"><span class="clip"></span><div class="shot" role="img" aria-label="Group of friends on an outing together"></div></figure>
  <figure class="snapshot snap-4"><span class="clip"></span><div class="shot" role="img" aria-label="Members enjoying a garden visit"></div></figure>

  <svg class="ribbon" viewBox="0 0 568 60" aria-hidden="true">
    <polygon points="0,0 568,0 548,30 568,60 0,60 20,30" fill="var(--ribbon)"/>
    <polygon points="8,5 560,5 543,30 560,55 8,55 25,30" fill="none" stroke="#8a8a8a" stroke-width="2"/>
  </svg>
  <p class="ribbon-text">We also host PHOTO CONTEST</p>

  <svg class="swoosh" viewBox="0 0 1200 170" aria-hidden="true">
    <path d="M300 150 Q800 60 1200 20" fill="none" stroke="var(--swoosh)" stroke-width="10"/>
    <path d="M420 165 Q850 90 1200 60" fill="none" stroke="#bdbdbd" stroke-width="6"/>
    <path d="M560 170 Q900 120 1200 100" fill="none" stroke="var(--swoosh)" stroke-width="4"/>
  </svg>

  <section class="perks">
    <p class="perk perk-1"><em>Free</em> Membership!</p>
    <p class="perk perk-2">Tickets <em>Discount for Members</em></p>
    <p class="perk perk-3">Special <em>Events / Outings</em> everyday!</p>
    <p class="perk perk-4">Different <em>Faces of the World</em></p>
    <p class="perk perk-5">Know <em>Each Other!</em></p>
    <p class="perk perk-6">Friendship, Sharing, <em>Social Gathering</em></p>
  </section>

  <svg class="badge" viewBox="-118 -118 236 236" aria-label="Discount up to 35%">
    <polygon fill="var(--badge)" stroke="#eeeeee" stroke-width="3" points="0,-115 22,-96 49,-104 60,-78 88,-74 86,-46 110,-32 96,-8 112,18 88,30 92,58 64,64 56,92 30,88 12,112 -12,96 -38,108 -50,84 -78,86 -80,58 -106,46 -92,22 -112,0 -92,-22 -106,-46 -80,-58 -80,-86 -52,-84 -40,-108 -14,-96"/>
    <g transform="rotate(-22)" fill="#ffffff" font-family="Roboto Condensed, Arial Narrow, sans-serif" text-anchor="middle">
      <text y="-36" font-size="30">Discount</text>
      <text y="-8" font-size="30">Upto</text>
      <text y="52" font-size="68" font-weight="500">35%</text>
    </g>
  </svg>

  <div class="brand">
    <div class="mark"></div>
    <div class="name">Nookly Events</div>
  </div>

  <footer class="contact-bar">
    <div class="contact contact-mail">
      <svg width="40" height="28" viewBox="0 0 40 28" aria-hidden="true">
        <rect x="1" y="1" width="38" height="26" fill="#ffffff"/>
        <path d="M1 1 L20 16 L39 1" fill="none" stroke="var(--band)" stroke-width="3"/>
      </svg>
      <span>Enquires@wandernookly.com</span>
    </div>
    <div class="contact contact-web">
      <svg width="30" height="30" viewBox="0 0 30 30" aria-hidden="true">
        <circle cx="15" cy="15" r="13" fill="#ffffff"/>
        <ellipse cx="15" cy="15" rx="6" ry="13" fill="none" stroke="var(--band)" stroke-width="2"/>
        <line x1="2" y1="15" x2="28" y2="15" stroke="var(--band)" stroke-width="2"/>
      </svg>
      <span>www.WanderNookly.com</span>
    </div>
  </footer>
</main>
</body>
</html>
```